Working as a fashion agent, I'll close down on short term the company Garment Harbor BV, and will start a new one-man business under the name 'Studio Lindholm Nord'. Also a logo could be interesting to design, if possible?!
Industry/Entity Type
Fashion

```html
<!DOCTYPE html>
<html lang="en">
<head>
<meta charset="utf-8">
<title>Studio Lindholm Nord — Letterhead</title>
<link rel="stylesheet" href="https://fonts.googleapis.com/css2?family=Cinzel:wght@600&family=Open+Sans:wght@400;700&display=swap">
<style>
  :root {
    --paper: #ffffff;
    --blue: #5a78bf;
    --yellow: #f6bd1c;
    --brand-red: #d94a2a;
    --ink: #1c1c1c;
  }
  html, body {
    margin: 0;
    padding: 0;
    overflow: hidden;
    background: var(--paper);
  }
  .letterhead {
    position: relative;
    width: 849px;
    height: 1200px;
    background: var(--paper);
    overflow: hidden;
  }
  .corner {
    position: absolute;
    display: block;
  }
  .corner--top-left { left: 0; top: 0; }
  .corner--bottom-right { right: 0; bottom: 0; }
  .corner .fill-blue { fill: var(--blue); }
  .corner .fill-yellow { fill: var(--yellow); }

  .brand {
    position: absolute;
    top: 160px;
    left: 540px;
    width: 280px;
    text-align: center;
    font-family: "Cinzel", serif;
    font-weight: 600;
    font-size: 24px;
    letter-spacing: 0.5px;
    color: var(--brand-red);
    margin: 0;
  }

  .contact {
    position: absolute;
    left: 37px;
    top: 1134px;
    font-family: "Open Sans", sans-serif;
    font-size: 12px;
    line-height: 22px;
    color: var(--ink);
  }
  .contact__row { display: flex; }
  .contact__item { margin-right: 40px; }
  .contact__label { font-weight: 700; }
</style>
</head>
<body>
<main class="letterhead">
  <svg class="corner corner--top-left" width="260" height="320" viewBox="0 0 260 320" aria-hidden="true">
    <path class="fill-yellow" d="M200 0 H240 C150 60 60 170 0 310 V270 C40 150 120 60 200 0 Z"/>
    <path class="fill-blue" d="M0 0 H200 C120 60 40 150 0 270 Z"/>
  </svg>

  <h1 class="brand">Studio Lindholm Nord</h1>

  <div class="contact">
    <div class="contact__row">
      <span class="contact__item"><span class="contact__label">Add :</span> 24 Harbour Lane, 1071 Amsterdam, The Netherlands</span>
    </div>
    <div class="contact__row">
      <span class="contact__item"><span class="contact__label">E-mail :</span> info@lindholmnord.nl</span>
      <span class="contact__item"><span class="contact__label">Web</span> www.lindholmnord.nl</span>
    </div>
  </div>

  <svg class="corner corner--bottom-right" width="300" height="680" viewBox="549 520 300 680" aria-hidden="true">
    <path class="fill-yellow" d="M849 530 C825 800 710 1050 560 1200 H849 Z"/>
    <path class="fill-blue" d="M849 820 C805 1000 725 1120 645 1200 H849 Z"/>
  </svg>
</main>
</body>
</html>
```